Following list to be designed:

1. A4 Letter Head

Must comprise of:
BRISK HARBOR and its LOGO
Address: No.41, 2F, Telvin Court, Marlow Lane, Upper Fennel Gardens, Bangalore 560 078
Tel: 080 41927380
Fax: 080 41927381
Mail: hello@briskharbor.example

Color of wordings to be in the lighter shade of blue and brighter shade of blue.

2. A4 Envelope

Must comprise of:
BRISK HARBOR and its LOGO
Tel: 080 41927380
Fax: 080 41927381

3. Postal Envelope

Must comprise of:
BRISK HARBOR and its LOGO
Tel: 080 41927380
Fax: 080 41927381

4. Business Card

Must comprise of:
Ravi Menon
Managing Partner
Cell: +91 9847162053
Mail: ravimenon@briskharbor.example
Tel: 080 41927380
Fax: 080 41927381

5. A4 Letter Head

Must comprise of:
BRISK HARBOR CORP. (wording) and BRISK HARBOR LOGO (only blue ribbon)

Blue ribbon (BRISK HARBOR LOGO) may be placed on Left Top Corner of the A4 Letter Head
and BRISK HARBOR CORP. (wording) to be placed on Right Top Corner of the A4 Letter Head

Tel: 080 41927380
Fax: 080 41927381

6. . A4 Envelope

Must comprise of:

Blue ribbon (BRISK HARBOR LOGO) may be placed on Left Top Corner of the A4 Envelope
and BRISK HARBOR CORP. (wording) to be placed on Right Top Corner of the A4 Envelope
Tel: 080 41927380
Fax: 080 41927381

Target Market(s)

Top IT/ITES Organizations

Industry/Entity Type

Real Estate Development

Font styles to use
Serif
Sans Serif

Colors
33a6d7
0792cd
85cae6

Requirements
Should not have
• Playful font and color

```html
<!DOCTYPE html>
<html lang="en">
<head>
<meta charset="utf-8">
<title>Brisk Harbor — Business Card</title>
<link rel="stylesheet" href="https://fonts.googleapis.com/css2?family=Open+Sans:ital,wght@0,400;0,600;0,700;1,400&display=swap">
<style>
  :root {
    --stage: #2a2a2a;
    --paper: #ffffff;
    --ink: #4a4a4a;
    --ink-soft: #666666;
    --name-blue: #3f74a8;
    --brand-blue: #3f7fb8;
    --brand-light: #5fb3dc;
    --band-gray: #6b6d6c;
    --rule: #8a8a8a;
    --faint: #eef1f4;
  }
  * { box-sizing: border-box; margin: 0; padding: 0; }
  html, body { width: 1200px; height: 987px; overflow: hidden; }
  body {
    background: var(--stage);
    font-family: "Open Sans", Arial, sans-serif;
    position: relative;
  }
  .card {
    position: absolute;
    left: 293px;
    width: 615px;
    height: 352px;
    overflow: hidden;
  }
  /* Front */
  .card--front { top: 130px; background: var(--paper); }
  .front__decor {
    position: absolute; left: 0; top: 0;
    width: 340px; height: 318px;
    background: linear-gradient(90deg, var(--faint) 0%, rgba(238,241,244,0.6) 60%, rgba(238,241,244,0) 100%);
  }
  .brand-name {
    position: absolute;
    right: 33px;
    font-weight: 600;
    letter-spacing: 0.5px;
    white-space: nowrap;
  }
  .card--front .brand-name { top: 104px; font-size: 27px; color: var(--ink-soft); }
  .person {
    position: absolute; left: 25px; top: 150px;
  }
  .person__name { font-size: 22px; font-weight: 600; color: var(--name-blue); line-height: 1.1; }
  .person__title { font-size: 16px; color: var(--ink-soft); margin-top: 3px; }
  .divider {
    position: absolute; left: 25px; top: 206px;
    width: 557px; height: 1px; background: var(--rule);
  }
  .contacts {
    position: absolute; left: 25px; top: 215px;
    list-style: none; font-size: 15px; color: var(--ink); line-height: 24px;
  }
  .contacts li { display: flex; align-items: center; gap: 8px; }
  .contacts svg { width: 15px; height: 15px; fill: var(--brand-blue); flex: none; }
  .address {
    position: absolute; right: 33px; top: 215px;
    font-size: 15px; color: var(--ink); line-height: 22px; text-align: right; font-style: normal;
  }
  .band-gray {
    position: absolute; left: 0; top: 331px; width: 380px; height: 11px;
    background: var(--band-gray);
  }
  .band-blue {
    position: absolute; right: 0; top: 318px; width: 250px; height: 34px;
    background: linear-gradient(90deg, var(--brand-light), var(--brand-blue));
    clip-path: polygon(20px 0, 100% 0, 100% 100%, 0 100%);
  }
  .band-blue__url {
    position: absolute; right: 28px; top: 6px;
    font-size: 15px; font-style: italic; letter-spacing: 1.5px; color: #fff;
  }
  /* Back */
  .card--back {
    top: 505px;
    background: radial-gradient(ellipse at 55% 35%, #63b4dd 0%, #4d8fc2 45%, #3f74a8 100%);
  }
  .back__art {
    position: absolute; left: 0; top: 0;
    width: 390px; height: 352px;
    background: linear-gradient(90deg, rgba(98,191,230,0.55) 0%, rgba(74,142,196,0.35) 65%, rgba(74,142,196,0) 100%);
  }
  .card--back .brand-name { top: 44px; font-size: 24px; color: #fff; }
  .back__url {
    position: absolute; right: 33px; top: 90px;
    font-size: 15px; font-style: italic; letter-spacing: 2.5px; color: #fff;
  }
</style>
</head>
<body>
  <section class="card card--front">
    <div class="front__decor" role="img" aria-label="Faint brand decoration area"></div>
    <div class="brand-name">BRISK HARBOR</div>
    <div class="person">
      <div class="person__name">Ravi Menon</div>
      <div class="person__title">Managing Partner</div>
    </div>
    <div class="divider"></div>
    <ul class="contacts">
      <li><svg viewBox="0 0 16 16"><path d="M3.6 1.5l2.2 2.6-1.3 1.8c.8 1.9 2.4 3.5 4.3 4.4l1.8-1.3 2.6 2.2-1.4 2.8C6.4 13.7 2 9.3 1 3.3z"/></svg>080 41927380</li>
      <li><svg viewBox="0 0 16 16"><path d="M4.5 1h7a1 1 0 0 1 1 1v12a1 1 0 0 1-1 1h-7a1 1 0 0 1-1-1V2a1 1 0 0 1 1-1zm.5 2v9h6V3zm3 9.7a.7.7 0 1 0 0 1.4.7.7 0 0 0 0-1.4z"/></svg>+91 9847162053</li>
      <li><svg viewBox="0 0 16 16"><path d="M4 1h8v4H4zM1.5 6h13a1 1 0 0 1 1 1v5h-3v3h-9v-3h-3V7a1 1 0 0 1 1-1zM5 11v3h6v-3z"/></svg>080 41927381</li>
      <li><svg viewBox="0 0 16 16"><path d="M1 3h14v10H1zm1.3 1.2L8 8.5l5.7-4.3z"/></svg>ravimenon@briskharbor.example</li>
    </ul>
    <address class="address">
      No.41, 2F, Telvin Court<br>
      Marlow Lane<br>
      Upper Fennel Gardens<br>
      Bangalore 560 078
    </address>
    <div class="band-gray"></div>
    <div class="band-blue"><span class="band-blue__url">www.briskharbor.example</span></div>
  </section>

  <section class="card card--back">
    <div class="back__art" role="img" aria-label="Large blue brand artwork area"></div>
    <div class="brand-name">BRISK HARBOR</div>
    <div class="back__url">www.briskharbor.example</div>
  </section>
</body>
</html>
```